New Business Card for Web Design/Internet Marketing Company

Looking for a great looking new business card. We are a 10 year old web design, internet marketing and website management company that works mostly with small businesses.

Our new card needs to better match the colors and style of our website, be bold, extremely usable and slightly edgy.

Target Market(s)

Small/Medium businesses that have websites

Industry/Entity Type

Internet

Requirements
Must have
• Front and back design, full color, rounded corners please

Must use the colors/style of our website (JPG provided)

INFO FOR CARDS (as readable as possible please)
Mark Tilden
President/CEO
mark@brivatnet.example
Phone: 520-318-7051
Toll Free: 866-318-7051
Address: 4125 W. Larkspur Ave. Ste. 160, Tucson, AZ 85799

THINGS I WANT TO PROMOTE (if there is room):
1. Our Website - www.brivatnet.example

2. Social Media
Twitter: @brivatnet
Facebook: www.facebook.com/brivatnet

3. Our Services
Web Design
Internet Marketing
Website Management

```html
<!DOCTYPE html>
<html lang="en">
<head>
<meta charset="utf-8">
<title>Brivatnet Business Card</title>
<link rel="stylesheet" href="https://fonts.googleapis.com/css2?family=Ubuntu:ital,wght@0,400;0,500;1,400&display=swap">
<style>
  :root {
    --page-bg: #dcedf7;
    --card-navy: #1b3a66;
    --band-sky: #66cdf5;
    --band-blue: #1a6fb5;
    --band-orange: #f58a34;
    --text-navy: #14325c;
    --text-white: #ffffff;
    --address-blue: #2a8fd0;
  }
  * { margin: 0; padding: 0; box-sizing: border-box; }
  html, body {
    width: 1200px;
    height: 900px;
    overflow: hidden;
    background: var(--page-bg);
    font-family: "Ubuntu", sans-serif;
  }
  .business-card {
    position: absolute;
    left: 128px;
    top: 176px;
    width: 944px;
    height: 544px;
    background: var(--card-navy);
    border-radius: 28px;
    overflow: hidden;
  }
  .band {
    position: absolute;
    left: 0;
    width: 472px;
    border-radius: 0 16px 16px 0;
  }
  .band-name {
    top: 62px;
    height: 92px;
    background: var(--band-sky);
    color: var(--text-navy);
    padding: 12px 0 0 142px;
  }
  .person-name { font-size: 29px; font-weight: 400; line-height: 36px; }
  .person-title { font-size: 23px; font-style: italic; line-height: 30px; }

  .band-contact {
    top: 224px;
    height: 134px;
    background: var(--band-blue);
    color: var(--text-white);
    padding-top: 16px;
  }
  .contact-row {
    display: flex;
    font-size: 24px;
    line-height: 34px;
  }
  .contact-label {
    width: 116px;
    text-align: right;
    font-style: italic;
  }
  .contact-value { margin-left: 26px; }

  .band-social {
    top: 374px;
    height: 130px;
    background: var(--band-orange);
    color: var(--text-navy);
    padding-top: 10px;
  }
  .social-row {
    display: flex;
    align-items: center;
    height: 38px;
    font-size: 24px;
  }
  .social-icon {
    width: 34px;
    height: 34px;
    margin-left: 82px;
    margin-right: 26px;
    flex: none;
  }
  .brand {
    position: absolute;
    left: 472px;
    width: 472px;
    top: 118px;
    display: flex;
    justify-content: center;
    align-items: center;
    gap: 16px;
  }
  .brand-dot {
    width: 40px;
    height: 40px;
    border-radius: 50%;
    background: var(--band-blue);
  }
  .brand-name {
    font-size: 58px;
    font-weight: 500;
    color: var(--band-orange);
    line-height: 1;
  }
  .services {
    position: absolute;
    left: 472px;
    width: 472px;
    top: 250px;
    list-style: none;
    text-align: center;
    color: var(--text-white);
    font-size: 24px;
    line-height: 37px;
  }
  .address {
    position: absolute;
    left: 472px;
    width: 472px;
    top: 420px;
    text-align: center;
    font-style: normal;
    color: var(--address-blue);
    font-size: 24px;
    line-height: 32px;
  }
</style>
</head>
<body>
  <article class="business-card">
    <section class="band band-name">
      <h1 class="person-name">Dale Renwick</h1>
      <p class="person-title">President/CEO</p>
    </section>

    <section class="band band-contact">
      <div class="contact-row"><span class="contact-label">email</span><span class="contact-value">dale@brivatnet.example</span></div>
      <div class="contact-row"><span class="contact-label">phone</span><span class="contact-value">520-318-7051</span></div>
      <div class="contact-row"><span class="contact-label">toll-free</span><span class="contact-value">866-318-7051</span></div>
    </section>

    <section class="band band-social">
      <div class="social-row">
        <svg class="social-icon" viewBox="0 0 34 34"><rect width="34" height="34" rx="4" fill="#1b3a66"/></svg>
        <span>/brivatnet</span>
      </div>
      <div class="social-row">
        <svg class="social-icon" viewBox="0 0 34 34"><rect width="34" height="34" rx="4" fill="#1b3a66"/></svg>
        <span>@brivatnet</span>
      </div>
      <div class="social-row">
        <svg class="social-icon" viewBox="0 0 34 34" fill="none">
          <circle cx="17" cy="17" r="15" fill="#1b3a66"/>
          <g stroke="#f58a34" stroke-width="2">
            <ellipse cx="17" cy="17" rx="6" ry="14"/>
            <line x1="3" y1="17" x2="31" y2="17"/>
            <line x1="17" y1="3" x2="17" y2="31"/>
            <path d="M6 10 H28 M6 24 H28"/>
          </g>
        </svg>
        <span>www.brivatnet.example</span>
      </div>
    </section>

    <div class="brand">
      <span class="brand-dot"></span>
      <span class="brand-name">brivatnet</span>
    </div>

    <ul class="services">
      <li>Web Design</li>
      <li>Internet Marketing</li>
      <li>Website Management</li>
    </ul>

    <address class="address">
      4125 W. Larkspur Ave. Ste. 160<br>
      Tucson, AZ 85799
    </address>
  </article>
</body>
</html>
```